Label and lid design for glas jogurt (dairy)

We need a new design for our glas jogurt with honey. For the lid and the label.

Reason: Hello We are finishing the project and would like the last designs and revision, so next week we can choose the one. thx! Regards

Switzerland, regional

• Name: Honig-Jogurt
• Marke: Wendlar (see the fox Logo in attachment, not use too dominant)
• Pictures Bees, Honeycomb, flowing honey (illustration prefered)
• Image/Values: Traditional, regional, classic, healty and very good honey jogurt produced by a local family enterprise founded in 1883
• Musts: Gewicht 125 g
• Nährwerttabelle
• Zutatenliste: Milch, Honig
• Molkerei Wendlar 9471 Rorschach
• Oval with CH 5816, see PDF
• Bei max. +6°C aufbewahren
• EAN
• Verbrauchen bis: (The position has to match the date printing field in the PDF attached and has to bee free to print datum on). Everything has to be written in German only.
• Measurings:
• Lid: 48mm with lace 36mm x 12mm, see PDF
• Label 26mm x 195mm
• The design you see in the attachment PDF has nothing to do with this project.
• A Variation for Nature and Strawberry Jogurt in the same glas cup and with same lid
• the design you see attached in the pdf

```html
<!DOCTYPE html>
<html lang="de">
<head>
<meta charset="utf-8">
<title>Honig Jogurt – Deckel und Etikett</title>
<link rel="stylesheet" href="https://fonts.googleapis.com/css2?family=Oswald:wght@500&family=Open+Sans:wght@600;700&display=swap">
<style>
  :root {
    --paper: #ffffff;
    --honey: #f5b400;
    --honey-light: #ffd52a;
    --honey-deep: #e89a00;
    --ink: #2a2a2a;
    --outline: #f7c21c;
    --brand-red: #e3161b;
    --tab-red: #ff0000;
    --sky-center: #ffffff;
    --sky-edge: #8cc4ea;
    --grass-light: #a6dc3c;
    --grass-deep: #4f9a16;
    --silver: #9a9a9a;
  }
  * { margin: 0; padding: 0; box-sizing: border-box; }
  html, body { width: 1200px; height: 675px; overflow: hidden; background: var(--paper); }
  .canvas { position: relative; width: 1200px; height: 675px; background: var(--paper); }

  .product-title {
    font-family: "Oswald", "Arial Narrow", sans-serif;
    font-weight: 500;
    color: var(--ink);
    line-height: 1;
    text-shadow:
      1px 0 0 var(--outline), -1px 0 0 var(--outline),
      0 1px 0 var(--outline), 0 -1px 0 var(--outline),
      1px 1px 0 var(--outline), -1px -1px 0 var(--outline),
      1px -1px 0 var(--outline), -1px 1px 0 var(--outline),
      2px 2px 2px rgba(0,0,0,.35);
  }
  .brand-name {
    font-family: "Open Sans", Arial, sans-serif;
    font-weight: 700;
    color: var(--brand-red);
    line-height: 1;
  }

  /* Lid */
  .lid { position: absolute; left: 716px; top: 71px; width: 160px; height: 290px; }
  .lid-tab { position: absolute; left: 59px; top: 140px; width: 42px; height: 146px; background: var(--tab-red); }
  .lid-tab::before {
    content: ""; position: absolute; left: -20px; top: -4px; width: 82px; height: 22px;
    background: var(--tab-red); border-radius: 0 0 50% 50% / 0 0 100% 100%;
  }
  .lid-face {
    position: absolute; left: 0; top: 0; width: 160px; height: 160px; border-radius: 50%; overflow: hidden;
    background: radial-gradient(circle at 50% 42%, var(--sky-center) 0%, #e6f3fb 35%, var(--sky-edge) 100%);
  }
  .lid-grass {
    position: absolute; left: 0; bottom: 0; width: 100%; height: 30px;
    background: linear-gradient(to bottom, var(--grass-light), var(--grass-deep));
  }
  .lid-brand { position: absolute; top: 28px; left: 0; width: 100%; text-align: center; font-size: 8px; }
  .lid-title { position: absolute; left: 38px; top: 42px; font-size: 19px; }
  .lid-title .line-two { display: block; padding-left: 20px; margin-top: 2px; }
  .lid-comb {
    position: absolute; left: 40px; top: 80px; width: 26px; height: 28px; border-radius: 6px;
    background: radial-gradient(circle, var(--honey-light), var(--honey-deep));
  }
  .lid-facts {
    position: absolute; top: 114px; left: 0; width: 100%; text-align: center;
    font-family: "Open Sans", Arial, sans-serif; font-weight: 600; font-size: 4.6px; line-height: 1.5; color: var(--ink);
  }

  /* Label */
  .label { position: absolute; left: 453px; top: 425px; width: 696px; height: 93px; overflow: hidden; }
  .label-art { position: absolute; inset: 0; width: 100%; height: 100%; }
  .label-dipper {
    position: absolute; left: 265px; top: 28px; width: 22px; height: 40px; border-radius: 10px 10px 4px 4px;
    background: linear-gradient(to bottom, #f0a800, #b86a00);
  }
  .label-title { position: absolute; left: 302px; top: 17px; font-size: 16px; }
  .label-title .line-two { display: block; padding-left: 10px; margin-top: 1px; }
  .label-comb {
    position: absolute; left: 300px; top: 47px; width: 20px; height: 22px; border-radius: 5px;
    background: radial-gradient(circle, var(--honey-light), var(--honey-deep));
  }
  .label-brand { position: absolute; left: 354px; top: 26px; font-size: 6px; }
</style>
</head>
<body>
<main class="canvas">

  <section class="lid" aria-label="Deckel">
    <div class="lid-tab"></div>
    <div class="lid-face">
      <div class="lid-grass" role="img" aria-label="Grüne Wiese"></div>
      <div class="lid-brand brand-name">Wendlar</div>
      <h1 class="lid-title product-title">Honig<span class="line-two">Jogurt</span></h1>
      <div class="lid-comb" role="img" aria-label="Honigwaben"></div>
      <p class="lid-facts">Zutatenliste: Milch, Honig<br>Gewicht 125 g</p>
    </div>
  </section>

  <section class="label" aria-label="Etikett">
    <svg class="label-art" viewBox="0 0 696 93" preserveAspectRatio="none" aria-hidden="true">
      <defs>
        <linearGradient id="honeyBand" x1="0" y1="0" x2="0" y2="1">
          <stop offset="0" stop-color="var(--honey-deep)"/>
          <stop offset="1" stop-color="var(--honey-light)"/>
        </linearGradient>
        <linearGradient id="grassBand" x1="0" y1="0" x2="0" y2="1">
          <stop offset="0" stop-color="var(--grass-light)"/>
          <stop offset="1" stop-color="var(--grass-deep)"/>
        </linearGradient>
      </defs>
      <rect width="696" height="93" fill="url(#honeyBand)"/>
      <path d="M0,48 C90,20 220,14 320,14 C450,14 520,42 640,64 C670,69 688,70 696,70 L696,93 L0,93 Z" fill="var(--paper)"/>
      <path d="M0,50 C90,22 200,16 290,16" fill="none" stroke="var(--silver)" stroke-width="1.5"/>
      <path d="M330,16 C450,16 520,45 640,67 C670,72 688,73 696,73" fill="none" stroke="var(--silver)" stroke-width="2"/>
      <rect y="64" width="696" height="29" fill="url(#grassBand)" role="img" aria-label="Grüne Wiese"/>
    </svg>
    <div class="label-dipper" role="img" aria-label="Honiglöffel mit fliessendem Honig"></div>
    <h2 class="label-title product-title">Honig<span class="line-two">Jogurt</span></h2>
    <div class="label-comb" role="img" aria-label="Honigwaben"></div>
    <div class="label-brand brand-name">Wendlar</div>
  </section>

</main>
</body>
</html>
```